Erotik Online Shop
Zielgruppe
Kunden des Online Shops, vorzugsweise schwule Männer wobei der Shop auch die hetero Ziegruppe bedienen bzw. befriedigen kann.
Aufgabenstellung
Für den Relounch unserers Online Shops benötigen wir mehrer Grafiken für die Startseite des Shops sowie eventuell einen Überabreitung unseres Logos.

```html
<!DOCTYPE html>
<html lang="de">
<head>
<meta charset="utf-8">
<title>pxlmo for Flirtwerk7 – Shop-Grafiken</title>
<link rel="stylesheet" href="https://fonts.googleapis.com/css2?family=Russo+One&family=Oswald:wght@400;500;700&display=swap">
<style>
  :root {
    --red: #c8161d;
    --black: #0d0d0d;
    --dark: #1f1f1f;
    --mid: #3a3a3a;
    --light: #e9e9e9;
    --white: #ffffff;
    --tick: #2fb52f;
  }
  * { box-sizing: border-box; margin: 0; padding: 0; }
  html, body { width: 1200px; height: 862px; overflow: hidden; background: var(--white); }
  .canvas { position: relative; width: 1200px; height: 862px; background: var(--white); font-family: "Oswald", sans-serif; }
  .abs { position: absolute; }
  .head { font-family: "Russo One", sans-serif; text-transform: uppercase; line-height: 1; white-space: nowrap; }
  .cond { font-family: "Oswald", sans-serif; font-weight: 700; text-transform: uppercase; line-height: 1; white-space: nowrap; }

  /* Hero banner */
  .hero { left: 52px; top: 40px; width: 668px; height: 347px; border-radius: 8px; background: var(--white); border: 1px solid #dcdcdc; overflow: hidden; box-shadow: 0 1px 4px rgba(0,0,0,.12); }
  .hero-photo { left: 383px; top: 0; width: 285px; height: 347px; background: linear-gradient(90deg, #fff 0%, #cfcfcf 25%, #9a9a9a 60%, #d8d8d8 100%); }
  .tag { background: var(--black); color: var(--white); padding: 8px 8px 8px; }
  .tag .hot { color: var(--red); }
  .tag-toys { left: 42px; top: 47px; font-size: 40px; }
  .line-for { left: 53px; top: 122px; font-size: 24px; color: var(--black); }
  .tag-boys { left: 106px; top: 105px; font-size: 50px; padding: 12px 10px; }
  .and-girls { left: 278px; top: 186px; font-size: 14px; font-weight: 700; color: var(--black); white-space: nowrap; }
  .hero-cta { left: 16px; top: 306px; font-size: 24px; color: var(--black); }
  .hero-cta .now { color: var(--red); }

  /* Credit */
  .credit { right: 87px; top: 100px; text-align: right; font-size: 55px; color: var(--black); line-height: 75px; }

  /* Tall banners */
  .tall { top: 501px; width: 151px; height: 294px; border-radius: 4px; background: linear-gradient(180deg, #2a2a2a, #121212); overflow: hidden; text-align: center; color: var(--white); box-shadow: 0 1px 4px rgba(0,0,0,.3); }
  .pay { left: 52px; }
  .pay .t1 { margin-top: 8px; font-size: 18px; color: var(--red); }
  .pay .t2 { margin-top: 6px; font-size: 17px; letter-spacing: 2px; }
  .methods { display: grid; grid-template-columns: 1fr 1fr; gap: 10px 8px; margin: 18px 12px 0; }
  .method { display: flex; align-items: center; justify-content: center; height: 34px; background: var(--light); border-radius: 3px; color: var(--mid); font-family: "Oswald", sans-serif; font-weight: 700; font-size: 12px; text-transform: uppercase; }
  .pay .t3 { margin-top: 22px; font-size: 15px; letter-spacing: 1px; }
  .pay .t4 { margin-top: 6px; font-size: 15px; color: var(--red); }
  .pay .t5 { margin-top: 8px; font-size: 10px; letter-spacing: 1px; }
  .pay .t6 { margin-top: 6px; font-size: 17px; letter-spacing: 2px; }

  .news { left: 223px; }
  .news .n1 { margin-top: 12px; font-size: 54px; letter-spacing: 1px; }
  .news .n2 { margin-top: 2px; font-size: 46px; color: var(--red); letter-spacing: 1px; }
  .news .n3 { margin-top: 8px; font-family: "Russo One", sans-serif; font-size: 12px; letter-spacing: 5px; }
  .field { display: block; margin: 0 auto; width: 132px; height: 23px; background: var(--white); color: #444; font-size: 11px; text-align: left; padding: 4px 6px; }
  .field-name { margin-top: 44px; }
  .field-mail { margin-top: 8px; }
  .register { margin: 16px auto 0; width: 132px; height: 24px; background: var(--red); border: 1px solid #fff; font-family: "Russo One", sans-serif; font-size: 12px; padding-top: 4px; letter-spacing: 1px; text-transform: uppercase; }

  .partner { left: 394px; }
  .partner-head { height: 54px; background: linear-gradient(180deg, #e01e25, #8e0f13); padding-top: 3px; font-size: 25px; line-height: 24px; letter-spacing: 1px; }
  .partner-photo { height: 104px; background: linear-gradient(180deg, #5a5a5a, #2a2a2a); }
  .step { margin: 0 auto; width: 136px; height: 25px; border: 2px solid var(--white); background: var(--black); font-family: "Oswald", sans-serif; font-weight: 500; font-size: 14px; line-height: 19px; text-transform: uppercase; white-space: nowrap; letter-spacing: .5px; }
  .step-first { margin-top: 9px; }
  .arrow { display: block; margin: 0 auto; }
  .payout { margin: 2px auto 0; width: 140px; height: 27px; background: var(--red); font-family: "Oswald", sans-serif; font-weight: 700; font-size: 17px; line-height: 27px; text-transform: uppercase; white-space: nowrap; }

  /* Safer shopping banner */
  .safer { left: 678px; top: 508px; width: 446px; height: 280px; border-radius: 5px; overflow: hidden; background: linear-gradient(90deg, #6b6b6b 0%, #2b2b2b 35%, #161616 100%); box-shadow: 0 1px 4px rgba(0,0,0,.3); }
  .safer-photo { left: 0; top: 0; width: 200px; height: 280px; background: linear-gradient(90deg, #8a8a8a, #505050 60%, rgba(30,30,30,0)); }
  .safer-kicker { right: 14px; top: 20px; font-size: 20px; color: var(--white); }
  .safer-title { left: 120px; top: 58px; width: 312px; height: 51px; background: var(--white); color: var(--red); font-size: 38px; text-align: center; line-height: 51px; letter-spacing: .5px; }
  .perks { right: 12px; top: 124px; list-style: none; }
  .perks li { display: flex; justify-content: flex-end; align-items: center; gap: 10px; height: 28px; color: var(--white); font-family: "Russo One", sans-serif; font-size: 14px; text-transform: uppercase; white-space: nowrap; }
</style>
</head>
<body>
<div class="canvas">

  <section class="hero abs" aria-label="Hero-Banner">
    <div class="hero-photo abs" role="img" aria-label="Schwarzweiß-Foto eines muskulösen Mannes in weißen Boxershorts"></div>
    <div class="tag tag-toys abs head"><span class="hot">Hot</span> Toys</div>
    <div class="line-for abs head">for</div>
    <div class="tag tag-boys abs head"><span class="hot">Hot</span> Boys</div>
    <div class="and-girls abs">(AND GIRLS)</div>
    <div class="hero-cta abs head">Come and get them. <span class="now">Now!</span></div>
  </section>

  <div class="credit abs head">pxlmo<br>for<br>Flirtwerk7</div>

  <section class="tall pay abs head" aria-label="Zahlungsarten">
    <div class="t1">100% sicher</div>
    <div class="t2">zahlen mit:</div>
    <div class="methods">
      <span class="method">Carta</span>
      <span class="method">Pagora</span>
      <span class="method">Direkto</span>
      <span class="method">Walleta</span>
    </div>
    <div class="t3">Keine Karte?</div>
    <div class="t4">Kein Problem!</div>
    <div class="t5">Wir akzeptieren</div>
    <div class="t6">Vorkasse</div>
  </section>

  <section class="tall news abs" aria-label="Newsletter">
    <div class="n1 cond">News</div>
    <div class="n2 cond">Letter</div>
    <div class="n3">100% FREE</div>
    <span class="field field-name">Name</span>
    <span class="field field-mail">email Adresse</span>
    <div class="register">Register now</div>
  </section>

  <section class="tall partner abs" aria-label="Partnerprogramm">
    <div class="partner-head cond">Partner<br>Programm</div>
    <div class="partner-photo" role="img" aria-label="Foto eines männlichen Oberkörpers in Jeans"></div>
    <div class="step step-first">Unser Banner</div>
    <svg class="arrow" width="22" height="20" viewBox="0 0 24 22"><path d="M8 0h8v11h8L12 22 0 11h8z" fill="#fff"/></svg>
    <div class="step">Deine Homepage</div>
    <svg class="arrow" width="22" height="20" viewBox="0 0 24 22"><path d="M8 0h8v11h8L12 22 0 11h8z" fill="#fff"/></svg>
    <div class="payout">$ Dein Geld $</div>
  </section>

  <section class="safer abs" aria-label="Safer Shopping">
    <div class="safer-photo abs" role="img" aria-label="Schwarzweiß-Foto eines nackten männlichen Oberkörpers"></div>
    <div class="safer-kicker abs head">Bei uns nie ohne...</div>
    <div class="safer-title abs cond">Safer Shopping</div>
    <ul class="perks abs">
      <li>Geld-zurück Garantie <svg width="20" height="18" viewBox="0 0 20 18"><path d="M2 9l5 6L18 2" fill="none" stroke="#2fb52f" stroke-width="4"/></svg></li>
      <li>Diskrete Verpackung <svg width="20" height="18" viewBox="0 0 20 18"><path d="M2 9l5 6L18 2" fill="none" stroke="#2fb52f" stroke-width="4"/></svg></li>
      <li>Kein Mindestbestellwert <svg width="20" height="18" viewBox="0 0 20 18"><path d="M2 9l5 6L18 2" fill="none" stroke="#2fb52f" stroke-width="4"/></svg></li>
      <li>Faire &amp; günstige Versandkosten <svg width="20" height="18" viewBox="0 0 20 18"><path d="M2 9l5 6L18 2" fill="none" stroke="#2fb52f" stroke-width="4"/></svg></li>
      <li>Onlineshopping seit 1999! <svg width="20" height="18" viewBox="0 0 20 18"><path d="M2 9l5 6L18 2" fill="none" stroke="#2fb52f" stroke-width="4"/></svg></li>
    </ul>
  </section>

</div>
</body>
</html>
```